Business Card - Self Employed Director

My husband needs a business card design. 2 sided printing required.

He is self employed, in the vineyard management and renewable energy sectors (see below for more information) and design and accent colors should reflect this.

Design should be modern but classic and professional too.

Card to show personal contact information only. Exact information subject to confirmation on finalizing design as we are moving soon and need to confirm the exact details.

Dorian Fellowes
email: dorian.fellowes@quillbarrow.example
mobile: 021 048 53117
home: +64 (0) 3 6142 875
184 Corbin Ridge Rise, RD4 Fenwold, Tasmeer, NZ 7460

I like the attached design by Pik for inspiration.

The reverse side should show name in bottom right corner with the pattern possibly reflecting renewable energy? Waves? Wind? Sea green, teal? Fresh, clean
Image on reverse should not be a photograph but a clean graphic based print on white background. Sans serfic fonts, Charcoal grey not black with accent colors reflected on the back?

Print ready artwork will be required. Please ask any questions :-) THANKS

Printing

Font styles to use
Sans Serif

Colors
86cfc6
ffffff
85abd2

Requirements
Must have
• Contact information as show
Should not have
• Anything cute, no red. No fancy flourish fonts.

```html
<!DOCTYPE html>
<html lang="en">
<head>
<meta charset="utf-8">
<title>Dorian Fellowes — Business Card</title>
<link href="https://fonts.googleapis.com/css2?family=Lato:ital,wght@0,400;0,700;0,900;1,700&display=swap" rel="stylesheet">
<style>
  :root {
    --sky: #85abd2;
    --sea: #86cfc6;
    --white: #ffffff;
    --charcoal: #3a3d40;
    --stage: #e9ebee;
  }
  * { box-sizing: border-box; margin: 0; padding: 0; }
  html, body {
    width: 1200px; height: 926px; overflow: hidden;
    background: var(--stage);
    font-family: "Lato", sans-serif;
    color: var(--charcoal);
  }
  .sheet {
    width: 1200px; height: 926px;
    display: flex; flex-direction: column;
    align-items: center; justify-content: center; gap: 70px;
  }
  .card {
    position: relative;
    width: 600px; height: 343px;
    background: var(--white);
    box-shadow: 0 2px 10px rgba(0,0,0,0.12);
  }
  /* Front */
  .card--front { border: 7px solid var(--sky); padding: 34px 40px; }
  .holder-name { font-size: 31px; font-weight: 400; line-height: 1; letter-spacing: 0.2px; }
  .holder-name strong { font-weight: 900; }
  .holder-role { font-size: 12px; font-weight: 900; letter-spacing: 1px; margin-top: 4px; }
  .accent-dash { width: 22px; height: 3px; background: var(--sea); margin: 30px 0 8px; }
  .accent-dash--address { margin-top: 34px; }
  .contact-list { list-style: none; font-size: 15.5px; line-height: 1.4; letter-spacing: 0.4px; }
  .contact-list b { font-weight: 700; font-style: italic; }
  .postal-address { font-size: 16.5px; letter-spacing: 0.5px; }
  /* Back */
  .card--back { padding: 22px; }
  .energy-field {
    width: 100%; height: 100%;
    background: linear-gradient(90deg, rgba(133,171,210,0.35), rgba(134,207,198,0.35));
  }
  .name-band {
    position: absolute; right: 22px; top: 218px;
    width: 300px; height: 44px;
    background: linear-gradient(90deg, var(--sky), var(--sea));
    color: var(--white);
    font-size: 22px; line-height: 44px; padding-left: 20px;
    box-shadow: -2px 2px 4px rgba(0,0,0,0.12);
  }
  .name-band strong { font-weight: 900; }
</style>
</head>
<body>
<main class="sheet">
  <section class="card card--front" aria-label="Card front">
    <h1 class="holder-name"><strong>Dorian</strong> Fellowes</h1>
    <p class="holder-role">DIRECTOR</p>
    <div class="accent-dash"></div>
    <ul class="contact-list">
      <li><b>mobile:</b> 021 048 53117</li>
      <li><b>home:</b> +64 (0) 3 6142 875</li>
      <li><b>email:</b> dorian.fellowes@quillbarrow.example</li>
    </ul>
    <div class="accent-dash accent-dash--address"></div>
    <p class="postal-address">184 Corbin Ridge Rise, RD4 Fenwold, Tasmeer, NZ 7460</p>
  </section>

  <section class="card card--back" aria-label="Card back">
    <div class="energy-field" role="img" aria-label="Grid pattern of small lightning-bolt marks shading from sky blue to sea green"></div>
    <p class="name-band"><strong>Dorian</strong> Fellowes</p>
  </section>
</main>
</body>
</html>
```